Party invitation with a difference

I have recently turned 65, and I am holding a party for a number of my friends

I am looking for a stylish party invitation possibly in the guise of a rock concert admission ticket./ poster

promoting my band Blue Kettle who will be playing.at the party. We are a middle of the road covers band

I am turning 65 years so something like 65 and still Rocking ...

The party will run from 7.00pm until 11.00pm

Food platter and drink supplied.

No presents please

Date Saturday 30 June 2018
At Marlow & Fenn Restaurant, 718, Pebble Lane. Clevedon, Auckland 2617

RSVP to dennis.halloway@wirefold.co.nz

Target Market(s)

I have a guest list

Font styles to use

Colors

Designer to choose colors to be used in the design.

Requirements
Must have
• I will want to email the invitation to my guests as well as be able to print some off .
Nice to have
• The invitation is from Dennis and Marjorie Halloway
Should not have
• Not be flowery

```html
<!DOCTYPE html>
<html lang="en">
<head>
<meta charset="utf-8">
<title>Turning 65 – Party Invitation</title>
<link rel="stylesheet" href="https://fonts.googleapis.com/css2?family=Oswald:wght@400;600;700&family=Archivo:ital,wght@1,800&family=Roboto:wght@400;500;700&display=swap">
<style>
  :root {
    --ink: #111111;
    --paper-light: #d6dc8a;
    --paper-mid: #b6bf4a;
    --paper-dark: #8f9a2c;
    --band: #0b0b0b;
    --band-text: #ffffff;
    --rule: #1a1a1a;
  }
  html, body {
    margin: 0;
    padding: 0;
    width: 1200px;
    height: 601px;
    overflow: hidden;
    background: #ffffff;
  }
  .ticket {
    position: relative;
    width: 1200px;
    height: 601px;
    overflow: hidden;
    color: var(--ink);
    background:
      radial-gradient(ellipse at 55% 45%, var(--paper-light) 0%, rgba(214,220,138,0) 60%),
      radial-gradient(ellipse at 90% 90%, var(--paper-dark) 0%, rgba(143,154,44,0) 55%),
      radial-gradient(ellipse at 20% 10%, var(--paper-dark) 0%, rgba(143,154,44,0) 45%),
      var(--paper-mid);
  }
  .side-band {
    position: absolute;
    left: 0; top: 0;
    width: 124px;
    height: 601px;
    background: var(--band);
  }
  .side-band__title {
    position: absolute;
    left: 62px;
    top: 300px;
    transform: translate(-50%, -50%) rotate(-90deg);
    white-space: nowrap;
    font-family: "Oswald", sans-serif;
    font-weight: 700;
    font-size: 78px;
    letter-spacing: 4px;
    color: var(--band-text);
    line-height: 1;
  }
  .host-intro {
    position: absolute;
    left: 212px; width: 946px;
    top: 30px;
    text-align: center;
    font-family: "Oswald", sans-serif;
    font-weight: 400;
    font-size: 50px;
    letter-spacing: 1px;
    line-height: 1;
  }
  .host-names {
    position: absolute;
    left: 212px; width: 946px;
    top: 102px;
    text-align: center;
    font-family: "Oswald", sans-serif;
    font-weight: 700;
    font-size: 52px;
    letter-spacing: 1.5px;
    line-height: 1;
  }
  .rule {
    position: absolute;
    background: var(--rule);
  }
  .rule--top { left: 212px; top: 193px; width: 946px; height: 2px; }
  .rule--divider { left: 452px; top: 193px; width: 2px; height: 386px; }
  .rule--day { left: 452px; top: 283px; width: 706px; height: 2px; }
  .rule--venue { left: 452px; top: 398px; width: 706px; height: 2px; }
  .date {
    position: absolute;
    left: 212px; width: 240px;
    text-align: center;
    line-height: 1;
  }
  .date__month {
    top: 222px;
    font-family: "Archivo", sans-serif;
    font-style: italic;
    font-weight: 800;
    font-size: 48px;
  }
  .date__day {
    top: 268px;
    font-family: "Oswald", sans-serif;
    font-weight: 700;
    font-size: 210px;
    letter-spacing: -4px;
  }
  .date__year {
    top: 506px;
    font-family: "Archivo", sans-serif;
    font-style: italic;
    font-weight: 800;
    font-size: 46px;
  }
  .weekday {
    position: absolute;
    left: 454px; width: 704px;
    top: 214px;
    text-align: center;
    font-family: "Roboto", sans-serif;
    font-weight: 700;
    font-size: 44px;
    letter-spacing: 2px;
    line-height: 1;
  }
  .venue {
    position: absolute;
    left: 454px; width: 704px;
    text-align: center;
    font-family: "Roboto", sans-serif;
    line-height: 1;
  }
  .venue__name { top: 300px; font-weight: 500; font-size: 34px; }
  .venue__address { top: 352px; font-weight: 400; font-size: 21px; }
  .band-mark {
    position: absolute;
    left: 454px; width: 704px;
    top: 460px;
    display: flex;
    justify-content: center;
    align-items: center;
    gap: 16px;
  }
  .band-mark__square {
    width: 30px; height: 30px;
    background: var(--ink);
  }
  .band-mark__name {
    font-family: "Oswald", sans-serif;
    font-weight: 700;
    font-size: 54px;
    line-height: 1;
    color: var(--ink);
  }
</style>
</head>
<body>
  <main class="ticket">
    <aside class="side-band">
      <div class="side-band__title">TURNING 65</div>
    </aside>

    <p class="host-intro" style="margin:0">THE INVITATION IS FROM</p>
    <h1 class="host-names" style="margin:0">DENNIS AND MARJORIE HALLOWAY</h1>

    <div class="rule rule--top"></div>
    <div class="rule rule--divider"></div>
    <div class="rule rule--day"></div>
    <div class="rule rule--venue"></div>

    <div class="date date__month">JUNE</div>
    <div class="date date__day">30</div>
    <div class="date date__year">2018</div>

    <div class="weekday">SATURDAY</div>
    <div class="venue venue__name">At Marlow &amp; Fenn Restaurant,</div>
    <div class="venue venue__address">718, Pebble Lane.Clevedon, Auckland 2617</div>

    <div class="band-mark">
      <span class="band-mark__square"></span>
      <span class="band-mark__name">Blue Kettle</span>
    </div>
  </main>
</body>
</html>
```